Lowell Brandt

20 Year Licensed Master Barber specializing in:
men/women cuts, Grooming, Straight razor Shaving and tape line enhancement, beard grooming, eye brow enhancement, South of France, Hot Towel Treatments, Scalp, Blow outs, Shags, Custom Design,RazorCuts,Shear Cuts, Bobs, Perms, Relaxers, Shoe Shine.
Please create a wonderful business card incorporating all the info above and selecting one of the photos. Please be creative.

Barber

```html
<!DOCTYPE html>
<html lang="en">
<head>
<meta charset="utf-8">
<title>Lowell Brandt – Master Barber Business Card</title>
<link rel="stylesheet" href="https://fonts.googleapis.com/css2?family=Alice&family=Lato:ital,wght@0,400;0,700;1,700&display=swap">
<style>
  :root {
    --stage: #5a5a5a;
    --card-black: #0b0b0c;
    --panel-black: #18181a;
    --strip-grey: #9ea3a6;
    --barber-red: #d91f2d;
    --white: #ffffff;
    --photo-warm: #9a6a4c;
    --photo-dark: #2a1c16;
  }
  * { box-sizing: border-box; margin: 0; padding: 0; }
  html, body { width: 1200px; height: 1000px; overflow: hidden; }
  body {
    background: var(--stage);
    position: relative;
    font-family: "Lato", sans-serif;
    color: var(--white);
  }
  .card {
    position: absolute;
    left: 340px;
    width: 520px;
    height: 297px;
    background: var(--card-black);
    overflow: hidden;
  }
  .card--front { top: 135px; }
  .card--back { top: 515px; }
  .card__shapes { position: absolute; inset: 0; }

  .portrait-name {
    position: absolute;
    left: 36px;
    top: 220px;
    width: 202px;
    text-align: center;
  }
  .portrait-name__name {
    font-family: "Alice", serif;
    font-size: 28px;
    line-height: 1;
  }
  .portrait-name__title {
    font-weight: 700;
    font-style: italic;
    font-size: 20px;
    line-height: 1.1;
    margin-top: 3px;
  }
  .contact-list {
    position: absolute;
    right: 21px;
    top: 48px;
    list-style: none;
    text-align: right;
    font-size: 16px;
    line-height: 25px;
  }
  .brand-mark {
    position: absolute;
    left: 400px;
    top: 216px;
    width: 112px;
    font-size: 14px;
    font-weight: 700;
    white-space: nowrap;
  }

  .specialty-heading {
    position: absolute;
    left: 42px;
    top: 47px;
    color: var(--barber-red);
    font-size: 19.5px;
    font-weight: 700;
    font-style: italic;
    white-space: nowrap;
  }
  .service-list {
    position: absolute;
    top: 91px;
    list-style: none;
    font-size: 14px;
    line-height: 22.5px;
    white-space: nowrap;
  }
  .service-list li {
    position: relative;
    padding-left: 15px;
  }
  .service-list li::before {
    content: "•";
    position: absolute;
    left: 0;
    top: 0;
  }
  .service-list--left { left: 36px; }
  .service-list--right { left: 238px; }
</style>
</head>
<body>

  <section class="card card--front" aria-label="Business card front">
    <svg class="card__shapes" width="520" height="297" viewBox="0 0 520 297">
      <defs>
        <linearGradient id="portraitTone" x1="0" y1="0" x2="1" y2="1">
          <stop offset="0" stop-color="var(--photo-dark)"/>
          <stop offset="0.5" stop-color="var(--photo-warm)"/>
          <stop offset="1" stop-color="var(--photo-dark)"/>
        </linearGradient>
      </defs>
      <rect x="0" y="0" width="26" height="297" fill="var(--strip-grey)"/>
      <polygon points="190,0 205,0 258,297 243,297" fill="var(--panel-black)"/>
      <polygon points="26,0 190,0 243,297 26,297" fill="url(#portraitTone)"
               role="img" aria-label="Portrait photo of the barber in a tweed flat cap and glasses"/>
      <rect x="360" y="183" width="160" height="85" fill="var(--barber-red)"/>
      <line x1="360" y1="183.5" x2="520" y2="183.5" stroke="var(--white)" stroke-width="1.5"/>
      <line x1="360" y1="267.5" x2="520" y2="267.5" stroke="var(--white)" stroke-width="1.5"/>
      <circle cx="348" cy="225" r="43" fill="var(--white)"/>
    </svg>
    <div class="portrait-name">
      <p class="portrait-name__name">Lowell Brandt</p>
      <p class="portrait-name__title">Master Barber</p>
    </div>
    <ul class="contact-list">
      <li>Lowell.brandt3@mailbox.com</li>
      <li>(555)318-2046</li>
      <li>Snapfolio:3lbrandt</li>
      <li>Friendbook: YourPage</li>
    </ul>
    <p class="brand-mark">Lowell Brandt</p>
  </section>

  <section class="card card--back" aria-label="Business card back">
    <svg class="card__shapes" width="520" height="297" viewBox="0 0 520 297">
      <path d="M456,0 H520 V297 H368 C420,262 448,190 456,110 C460,60 460,25 456,0 Z" fill="var(--barber-red)"/>
      <path d="M476,0 C480,30 480,70 476,115 C468,195 440,262 388,297" fill="none" stroke="var(--card-black)" stroke-width="9"/>
      <g class="tool-badge">
        <circle cx="442" cy="142" r="33" fill="var(--white)" stroke="var(--card-black)" stroke-width="4"/>
        <g transform="rotate(35 442 142)" fill="var(--card-black)">
          <rect x="424" y="134" width="36" height="5" rx="1.5"/>
          <rect x="425" y="139" width="1.8" height="9"/>
          <rect x="429" y="139" width="1.8" height="9"/>
          <rect x="433" y="139" width="1.8" height="9"/>
          <rect x="437" y="139" width="1.8" height="9"/>
          <rect x="441" y="139" width="1.8" height="9"/>
          <rect x="445" y="139" width="1.8" height="7"/>
          <rect x="449" y="139" width="1.8" height="7"/>
          <rect x="453" y="139" width="1.8" height="7"/>
          <rect x="457" y="139" width="1.8" height="7"/>
        </g>
      </g>
      <g class="tool-badge">
        <circle cx="412" cy="226" r="33" fill="var(--white)" stroke="var(--card-black)" stroke-width="4"/>
        <g stroke="var(--card-black)" stroke-width="2" fill="none" stroke-linecap="round">
          <line x1="398" y1="208" x2="419" y2="232"/>
          <line x1="404" y1="206" x2="411" y2="232"/>
          <circle cx="414" cy="237" r="4"/>
          <circle cx="423" cy="235" r="4"/>
        </g>
      </g>
    </svg>
    <h2 class="specialty-heading">20 Year Licensed Master Barber specializing in</h2>
    <ul class="service-list service-list--left">
      <li>Hot Towel Treatments,</li>
      <li>Tape Line Enhancement</li>
      <li>South Of France</li>
      <li>Eyebrow Enhancement</li>
      <li>Men/women Haircuts</li>
      <li>Custom Design</li>
      <li>Razorcuts</li>
    </ul>
    <ul class="service-list service-list--right">
      <li>Scalp, Blow Outs, Shags</li>
      <li>Straight Razor Shaving</li>
      <li>Beard Grooming</li>
      <li>Shoe Shine</li>
      <li>Shear Cuts, Bobs</li>
      <li>Perms, Relaxers</li>
      <li>Grooming</li>
    </ul>
  </section>

</body>
</html>
```